mobile app - telecom industry

We are a tech/service company. Our product is a mobile application for physical site inspection called “Verko”. Our target industry is telecommunica...

Target Market(s)

telecommunication

Industry/Entity Type

Industry

Requirements
Must have
• Screen size Orbix 7 - Android
• Suggest 3 colors
• Design 9 pages

```html
<!DOCTYPE html>
<html lang="en">
<head>
<meta charset="utf-8">
<title>Verko – site inspection app screens</title>
<link href="https://fonts.googleapis.com/css2?family=Roboto:wght@400;500&display=swap" rel="stylesheet">
<style>
:root{
  --page:#ffffff;
  --blue:#729ceb;
  --blue-deep:#4a72d6;
  --blue-soft:#a9c4f5;
  --link:#4f7ddc;
  --red:#f4687a;
  --red-deep:#e8485f;
  --green:#2fe27e;
  --green-deep:#12c07a;
  --orange:#f7a21c;
  --ink:#333a45;
  --muted:#6b7280;
  --line:#dfe3ea;
  --save:#4cd964;
  --shade:rgba(20,22,28,.68);
}
*{box-sizing:border-box;margin:0;padding:0}
html,body{width:1027px;height:1200px;overflow:hidden;background:var(--page);font-family:"Roboto",sans-serif;color:var(--ink)}
.canvas{position:relative;width:1027px;height:1200px}
.screen{position:absolute;width:205px;height:365px;overflow:hidden;background:#fff;box-shadow:0 6px 14px rgba(0,0,0,.12)}
.status{position:absolute;top:0;left:0;right:0;height:16px;display:flex;justify-content:space-between;align-items:center;padding:0 6px;font-size:8px;color:#fff;z-index:3}
.appbar{position:absolute;top:16px;left:0;right:0;height:26px;display:flex;align-items:center;gap:8px;padding-left:8px;z-index:3}
.brand{font-size:14px;font-weight:500;color:#fff;letter-spacing:.5px}
.back{width:11px;height:11px}
.scene{position:absolute}
.btn{position:absolute;width:68px;height:46px;background:#fff;border-radius:8px;box-shadow:0 2px 4px rgba(0,0,0,.15);display:flex;flex-direction:column;align-items:center;justify-content:center;gap:5px;font-size:7.5px;color:var(--ink)}
.btn svg{width:14px;height:14px}
.hero{position:absolute;top:0;left:0;right:0;height:85px;z-index:1}
.hero-title{position:absolute;left:12px;top:55px;font-size:11.5px;color:#fff;z-index:3;font-weight:500}
.row{position:absolute;left:6px;right:8px;height:52px;border-bottom:1px solid var(--line);font-size:9.5px}
.row .code{position:absolute;left:11px;top:8px;color:var(--link)}
.row .date{position:absolute;left:11px;top:23px;color:var(--muted)}
.row .type{position:absolute;left:104px;top:8px;color:var(--ink)}
.row .num{position:absolute;left:104px;top:23px;color:var(--muted)}
.row .trash{position:absolute;right:14px;top:13px;width:10px;height:12px}
.formbar{position:absolute;top:0;left:0;right:0;height:45px;background:linear-gradient(#6f97e6,#8fb1ef)}
.item{position:absolute;left:6px;right:8px;height:109px;border-bottom:1px solid var(--line)}
.item .q{position:absolute;left:11px;top:12px;font-size:9.5px;color:var(--ink)}
.item .q b{font-weight:400;color:var(--link)}
.tools{position:absolute;left:11px;top:36px;display:flex;gap:17px}
.tools svg{width:11px;height:11px}
.comment{position:absolute;left:12px;right:8px;top:59px;height:14px;border-bottom:1px solid var(--blue);font-size:8px;color:var(--muted);display:flex;gap:9px;align-items:center;padding-left:4px}
.comment svg{width:9px;height:9px}
.save{position:absolute;left:10px;right:9px;top:330px;height:28px;background:var(--save);color:#fff;font-size:8.5px;display:flex;align-items:center;justify-content:center;border-radius:2px}
.shade{position:absolute;inset:0;background:var(--shade);z-index:4}
.dialog{position:absolute;left:15px;width:174px;top:120px;height:104px;background:#fff;border-radius:2px;z-index:5;display:flex;flex-direction:column;align-items:center;justify-content:center;gap:10px;font-size:9.5px;color:var(--ink)}
.dialog svg{width:40px;height:40px}
.hub{position:absolute;left:10px;top:228px;width:186px;height:125px}
.quad{position:absolute;width:91px;height:60px;background:#fff;display:flex;flex-direction:column;align-items:center;justify-content:center;gap:5px;font-size:7.5px}
.quad svg{width:13px;height:13px}
.core{position:absolute;left:57px;top:26px;width:72px;height:72px;border-radius:50%;background:#fff;border:4px solid var(--blue);display:flex;flex-direction:column;align-items:center;justify-content:center;gap:4px;font-size:7.5px}
.core svg{width:13px;height:13px}
</style>
</head>
<body>
<svg width="0" height="0" style="position:absolute">
  <defs>
    <symbol id="ico-open" viewBox="0 0 16 16"><rect x="2" y="1" width="12" height="14" rx="1" fill="#f44336"/><rect x="2" y="1" width="3" height="14" fill="#c62828"/></symbol>
    <symbol id="ico-close" viewBox="0 0 16 16"><rect x="1" y="2" width="14" height="12" rx="1" fill="#36c95a"/><path d="M5 5l6 6M11 5l-6 6" stroke="#fff" stroke-width="2"/></symbol>
    <symbol id="ico-create" viewBox="0 0 16 16"><circle cx="8" cy="8" r="7" fill="var(--orange)"/><path d="M8 4v8M4 8h8" stroke="#fff" stroke-width="2"/></symbol>
    <symbol id="ico-sync" viewBox="0 0 16 16"><path d="M13 6A5.5 5.5 0 0 0 3 6M3 10a5.5 5.5 0 0 0 10 0" fill="none" stroke="var(--blue-deep)" stroke-width="2"/><path d="M14 2v4h-4M2 14v-4h4" fill="none" stroke="var(--blue-deep)" stroke-width="2"/></symbol>
    <symbol id="ico-gear" viewBox="0 0 16 16"><circle cx="8" cy="8" r="5" fill="none" stroke="var(--blue-deep)" stroke-width="4" stroke-dasharray="2.2 1.7"/><circle cx="8" cy="8" r="4" fill="var(--blue-deep)"/><circle cx="8" cy="8" r="1.7" fill="#fff"/></symbol>
    <symbol id="ico-back" viewBox="0 0 12 12"><path d="M11 6H2M6 2L2 6l4 4" fill="none" stroke="#fff" stroke-width="1.4"/></symbol>
    <symbol id="ico-trash" viewBox="0 0 10 12"><path d="M1 2.5h8M3.5 2.5V1h3v1.5M2 2.5l.6 9h4.8l.6-9M4 4.5v5M6 4.5v5" fill="none" stroke="var(--link)" stroke-width=".9"/></symbol>
    <symbol id="ico-cam" viewBox="0 0 12 12"><rect x="1" y="3" width="10" height="7" rx="1" fill="var(--link)"/><rect x="4" y="2" width="4" height="2" fill="var(--link)"/><circle cx="6" cy="6.5" r="2" fill="#fff"/></symbol>
    <symbol id="ico-pin" viewBox="0 0 12 12"><path d="M6 11S2.5 7 2.5 4.5a3.5 3.5 0 0 1 7 0C9.5 7 6 11 6 11z" fill="var(--link)"/><circle cx="6" cy="4.5" r="1.3" fill="#fff"/></symbol>
    <symbol id="ico-gauge" viewBox="0 0 12 12"><path d="M10 6a4 4 0 1 1-4-4" fill="none" stroke="var(--link)" stroke-width="1.3"/><path d="M6 6l4-3" stroke="var(--link)" stroke-width="1.3"/></symbol>
    <symbol id="ico-angle" viewBox="0 0 12 12"><path d="M2 2l8 8H2" fill="none" stroke="var(--link)" stroke-width="1.3"/></symbol>
    <symbol id="ico-list" viewBox="0 0 12 12"><path d="M1 3h1M4 3h7M1 6h1M4 6h7M1 9h1M4 9h7" stroke="var(--link)" stroke-width="1.3"/></symbol>
    <symbol id="ico-pen" viewBox="0 0 10 10"><path d="M1 9l1-3 5-5 2 2-5 5z" fill="var(--link)"/></symbol>
  </defs>
</svg>

<div class="canvas">

  <!-- Splash -->
  <section class="screen" style="left:18px;top:16px">
    <div class="status"><span>TELA</span><span>88% 9:00AM</span></div>
    <div class="scene" role="img" aria-label="Telecom tower above a city skyline with clouds" style="left:0;top:0;width:205px;height:245px;background:linear-gradient(#6d97e8 0%,#8fb2f0 45%,#5a7fd4 70%,#ffffff 100%)"></div>
    <div style="position:absolute;left:0;right:0;top:272px;text-align:center;font-size:28px;font-weight:500;color:var(--blue-deep);letter-spacing:1px">Verko</div>
  </section>

  <!-- Home menu, column -->
  <section class="screen" style="left:251px;top:16px;background:var(--blue)">
    <div class="status"><span>TELA</span><span>88% 9:00AM</span></div>
    <div class="appbar"><svg class="back"><use href="#ico-back"/></svg><span class="brand">Verko</span></div>
    <div class="scene" role="img" aria-label="Telecom tower with antenna dishes over rolling hills" style="left:95px;top:70px;width:110px;height:295px;background:linear-gradient(160deg,#8fb1ef,#5f88de);border-radius:60px 0 0 0"></div>
    <div class="btn" style="left:11px;top:64px"><svg><use href="#ico-open"/></svg>Open WO</div>
    <div class="btn" style="left:11px;top:123px"><svg><use href="#ico-close"/></svg>Close WO</div>
    <div class="btn" style="left:11px;top:183px"><svg><use href="#ico-create"/></svg>Create WO</div>
    <div class="btn" style="left:11px;top:244px"><svg><use href="#ico-sync"/></svg>Syncronize</div>
    <div class="btn" style="left:11px;top:305px"><svg><use href="#ico-gear"/></svg>Settings</div>
  </section>

  <!-- Open work orders -->
  <section class="screen" style="left:485px;top:16px">
    <div class="status"><span>TELA</span><span>88% 9:00AM</span></div>
    <div class="hero" role="img" aria-label="Red header with tower and city skyline" style="background:linear-gradient(#f47a8a,var(--red-deep))"></div>
    <div class="appbar"><svg class="back"><use href="#ico-back"/></svg><span class="brand">Verko</span></div>
    <div class="hero-title">Open Work Orders</div>
    <div class="row" style="top:92px"><span class="code">TH1157-A</span><span class="date">2017-10-25</span><span class="type">TSSR</span><span class="num">525</span><svg class="trash"><use href="#ico-trash"/></svg></div>
    <div class="row" style="top:145px"><span class="code">TH1232-B</span><span class="date">2017-10-25</span><span class="type">SAR</span><span class="num">112</span><svg class="trash"><use href="#ico-trash"/></svg></div>
  </section>

  <!-- Home menu, two columns -->
  <section class="screen" style="left:762px;top:16px;background:var(--blue)">
    <div class="status"><span>TELA</span><span>88% 9:00AM</span></div>
    <div class="appbar"><svg class="back"><use href="#ico-back"/></svg><span class="brand">Verko</span></div>
    <div class="scene" role="img" aria-label="Telecom tower with antenna dishes over rolling hills" style="left:90px;top:70px;width:115px;height:230px;background:linear-gradient(160deg,#8fb1ef,#5f88de);border-radius:60px 0 0 0"></div>
    <div class="btn" style="left:16px;top:101px"><svg><use href="#ico-open"/></svg>Open WO</div>
    <div class="btn" style="left:16px;top:172px"><svg><use href="#ico-close"/></svg>Close WO</div>
    <div class="btn" style="left:16px;top:240px"><svg><use href="#ico-create"/></svg>Create WO</div>
    <div class="btn" style="left:16px;top:308px"><svg><use href="#ico-sync"/></svg>Syncronize</div>
    <div class="btn" style="left:120px;top:308px"><svg><use href="#ico-gear"/></svg>Settings</div>
  </section>

  <!-- Closed work orders -->
  <section class="screen" style="left:18px;top:414px">
    <div class="status"><span>TELA</span><span>88% 9:00AM</span></div>
    <div class="hero" role="img" aria-label="Green header with tower and city skyline" style="background:linear-gradient(var(--green),var(--green-deep))"></div>
    <div class="appbar"><svg class="back"><use href="#ico-back"/></svg><span class="brand">Verko</span></div>
    <div class="hero-title">Closed Work Orders</div>
    <div class="row" style="top:92px"><span class="code">TH2236-A</span><span class="date">2017-10-25</span><span class="type">SAR</span><span class="num">121</span><svg class="trash"><use href="#ico-trash"/></svg></div>
    <div class="row" style="top:145px"><span class="code">TH1538-C</span><span class="date">2017-9-18</span><span class="type">SAR</span><span class="num">224</span><svg class="trash"><use href="#ico-trash"/></svg></div>
  </section>

  <!-- Inspection form -->
  <section class="screen" style="left:251px;top:414px">
    <div class="status"><span>TELA</span><span>88% 9:00AM</span></div>
    <div class="formbar" role="img" aria-label="Blue header with small tower and clouds"></div>
    <div class="appbar"><svg class="back"><use href="#ico-back"/></svg><span class="brand">Verko</span></div>
    <div class="item" style="top:45px"><div class="q"><b>001-</b> TSSR&nbsp; Approved ?</div>
      <div class="tools"><svg><use href="#ico-cam"/></svg><svg><use href="#ico-pin"/></svg><svg><use href="#ico-gauge"/></svg><svg><use href="#ico-angle"/></svg><svg><use href="#ico-list"/></svg></div>
      <div class="comment"><svg><use href="#ico-pen"/></svg>Comment</div></div>
    <div class="item" style="top:154px"><div class="q"><b>002-</b> SAR Coordinate</div>
      <div class="tools"><svg><use href="#ico-cam"/></svg><svg><use href="#ico-pin"/></svg><svg><use href="#ico-gauge"/></svg><svg><use href="#ico-angle"/></svg><svg><use href="#ico-list"/></svg></div>
      <div class="comment"><svg><use href="#ico-pen"/></svg>Comment</div></div>
    <div class="save">Save and Close</div>
  </section>

  <!-- Saving -->
  <section class="screen" style="left:485px;top:414px">
    <div class="status"><span>TELA</span><span>88% 9:00AM</span></div>
    <div class="formbar" role="img" aria-label="Blue header with small tower and clouds"></div>
    <div class="appbar"><svg class="back"><use href="#ico-back"/></svg><span class="brand">Verko</span></div>
    <div class="item" style="top:45px"><div class="q"><b>001-</b> TSSR&nbsp; Approved ?</div>
      <div class="tools"><svg><use href="#ico-cam"/></svg><svg><use href="#ico-pin"/></svg><svg><use href="#ico-gauge"/></svg><svg><use href="#ico-angle"/></svg><svg><use href="#ico-list"/></svg></div>
      <div class="comment"><svg><use href="#ico-pen"/></svg>Comment</div></div>
    <div class="item" style="top:154px"><div class="q"><b>002-</b> SAR Coordinate</div>
      <div class="comment"><svg><use href="#ico-pen"/></svg>Comment</div></div>
    <div class="save">Save and Close</div>
    <div class="shade"></div>
    <div class="dialog">
      <svg viewBox="0 0 40 40"><g stroke="var(--blue-deep)" stroke-width="2.4" stroke-linecap="round">
        <path d="M20 4v7" opacity="1"/><path d="M31.3 8.7l-5 5" opacity=".9"/><path d="M36 20h-7" opacity=".8"/><path d="M31.3 31.3l-5-5" opacity=".7"/>
        <path d="M20 36v-7" opacity=".6"/><path d="M8.7 31.3l5-5" opacity=".5"/><path d="M4 20h7" opacity=".4"/><path d="M8.7 8.7l5 5" opacity=".3"/></g></svg>
      Saving your WO
    </div>
  </section>

  <!-- Home menu, hub -->
  <section class="screen" style="left:762px;top:414px;background:var(--blue)">
    <div class="status"><span>TELA</span><span>88% 9:00AM</span></div>
    <div class="appbar"><svg class="back"><use href="#ico-back"/></svg><span class="brand">Verko</span></div>
    <div class="scene" role="img" aria-label="Telecom tower with antenna dishes over rolling hills" style="left:0;top:50px;width:205px;height:178px;background:linear-gradient(#7aa2ec,#5f88de)"></div>
    <div class="hub">
      <div class="quad" style="left:0;top:0;border-radius:6px 0 0 0"><svg><use href="#ico-open"/></svg>Open WO</div>
      <div class="quad" style="left:95px;top:0;border-radius:0 6px 0 0"><svg><use href="#ico-close"/></svg>Close WO</div>
      <div class="quad" style="left:0;top:65px;border-radius:0 0 0 6px"><svg><use href="#ico-sync"/></svg>Syncronize</div>
      <div class="quad" style="left:95px;top:65px;border-radius:0 0 6px 0"><svg><use href="#ico-gear"/></svg>Settings</div>
      <div class="core"><svg><use href="#ico-create"/></svg>Create WO</div>
    </div>
  </section>

  <!-- Saved -->
  <section class="screen" style="left:18px;top:813px">
    <div class="status"><span>TELA</span><span>88% 9:00AM</span></div>
    <div class="formbar" role="img" aria-label="Blue header with small tower and clouds"></div>
    <div class="appbar"><svg class="back"><use href="#ico-back"/></svg><span class="brand">Verko</span></div>
    <div class="item" style="top:45px"><div class="q"><b>001-</b> TSSR&nbsp; Approved ?</div>
      <div class="tools"><svg><use href="#ico-cam"/></svg><svg><use href="#ico-pin"/></svg><svg><use href="#ico-gauge"/></svg><svg><use href="#ico-angle"/></svg><svg><use href="#ico-list"/></svg></div>
      <div class="comment"><svg><use href="#ico-pen"/></svg>Comment</div></div>
    <div class="item" style="top:154px"><div class="q"><b>002-</b> SAR Coordinate</div>
      <div class="comment"><svg><use href="#ico-pen"/></svg>Comment</div></div>
    <div class="save">Save and Close</div>
    <div class="shade"></div>
    <div class="dialog">
      <svg viewBox="0 0 40 40"><circle cx="20" cy="20" r="18" fill="none" stroke="var(--blue-soft)" stroke-width="1.5"/><path d="M11 20l7 7 13-14" fill="none" stroke="var(--blue-deep)" stroke-width="2.6" stroke-linecap="round" stroke-linejoin="round"/></svg>
      WO saved successfully
    </div>
  </section>

</div>
</body>
</html>
```